Illustrationen für Versicherungsunternehmen
Zielgruppe
Versicherungsunternehmen. Zielgruppen sind sowohl Firmen als auch Privatpersonen in jeder Altersklasse.
Die hier adressierte Zielgruppe sind moderndenkende, kreative Mitarbeiter.
Aufgabenstellung
Es geht um die Visualisierung eines Team-Manifests bestehend aus 15 Prinzipien. Diese sollen möglichst ansprechend, kreativ, aber auch nicht zu verspielt dargestellt werden. Außerdem soll die Darstellung auch noch das bereits vorhandene Projektlogo (Anhang) enthalten, dieses soll auch nicht im Vordergrund/Fokus stehen.
Ein Beispiel für eine ähnliche Visualisierung ist im Anhang beigefügt, diese entspricht optisch sehr stark den Vorstellungen. Es soll am Ende eine Vorlage für ein Plakat entstehen, welches man in unterschiedlichen Formaten (DIN 4 bis DIN 0) erstellen kann. Bei der Farbgebung sollte die dominierende Farbe blau (Blautöne) sein, ergänzt durch orangefarbene Akzente. Die 15 Prinzipien sind der 2.Anlage zu entnehmen.

```html
<!DOCTYPE html>
<html lang="de">
<head>
<meta charset="utf-8">
<title>Team-Manifest Plakat</title>
<link rel="stylesheet" href="https://fonts.googleapis.com/css2?family=Roboto+Condensed:wght@400;700;900&display=swap">
<style>
  :root{
    --blue:#1d5fa8;
    --blue-dark:#174c88;
    --orange:#e97a1f;
    --paper:#ffffff;
    --backdrop:#e9e8e6;
    --rule:#1d5fa8;
  }
  *{margin:0;padding:0;box-sizing:border-box}
  html,body{width:1200px;height:1200px;overflow:hidden;background:var(--backdrop)}
  body{font-family:"Roboto Condensed",Arial,sans-serif;color:var(--blue);text-transform:uppercase}
  .poster{
    position:absolute;left:215px;top:40px;width:770px;height:1120px;
    background:var(--paper);box-shadow:0 6px 24px rgba(0,0,0,.12);
    padding:90px 80px 40px;display:flex;flex-direction:column;gap:14px;
  }
  .row{display:flex;align-items:center;justify-content:center;gap:14px;line-height:1}
  .split{display:flex;align-items:stretch;justify-content:center;gap:16px}
  .split .divider{width:3px;background:var(--rule)}
  .block{display:flex;flex-direction:column;justify-content:center;gap:3px}
  .block.right{align-items:flex-start}
  .block.left{align-items:flex-end}
  .o{color:var(--orange)}
  .b{font-weight:900}
  .t34{font-size:38px}
  .t28{font-size:30px}
  .t24{font-size:25px}
  .t18{font-size:18px}
  .t14{font-size:14px;letter-spacing:.5px}
  .spaced{letter-spacing:6px}
  .icon{display:inline-block;flex:none;background:var(--blue);border-radius:4px;opacity:.85}
  .icon.orange{background:var(--orange)}
  .gemeinsam{font-size:52px;font-weight:900;color:var(--orange);letter-spacing:1px}
  .big{font-size:60px;font-weight:900}
  .trau{font-size:74px;font-weight:900}
  .stack-small{display:flex;flex-direction:column;font-size:13px;font-weight:700;line-height:1;margin:0 4px}
  .brand{margin-top:auto;display:flex;align-items:center;justify-content:center;gap:10px;text-transform:none}
  .brand .mark{width:22px;height:22px;background:var(--blue)}
  .brand .name{font-size:28px;font-weight:700;color:var(--blue)}
  .brand .sub{font-size:13px;font-weight:400;color:var(--blue);line-height:1.1;text-transform:uppercase}
</style>
</head>
<body>
<main class="poster">
  <div class="row t34">JEDES <span class="o b">ARGUMENT</span>
    <span class="icon orange" style="width:26px;height:34px" role="img" aria-label="Kleines Piktogramm einer Figur"></span>ZÄHLT</div>

  <div class="split">
    <div class="block left">
      <span class="t28">WIR HABEN</span>
      <span class="t28 o b">OFFENE</span>
      <span class="t28 o b">OHREN</span>
      <span class="t24">FÜR NEUES</span>
    </div>
    <div class="divider"></div>
    <div class="block right">
      <span class="t28"><span class="icon" style="width:24px;height:24px;vertical-align:middle" role="img" aria-label="Piktogramm Handschlag"></span> VERSPROCHEN IST</span>
      <span class="o b" style="font-size:42px">VERSPROCHEN</span>
      <span class="t18">WIR SIND ENTSCHEI-</span>
      <span class="t18 o b spaced">DUNGSFREUDIG</span>
    </div>
  </div>

  <div class="split">
    <div class="block left">
      <span class="gemeinsam">GEMEINSAM</span>
      <span class="t34">SIND WIR STÄRKER</span>
    </div>
    <div class="divider"></div>
    <div class="block right">
      <span class="t14">DIE PROBLEME<br>UNSERER KUNDEN</span>
      <span class="t18">SIND UNSERE</span>
      <span class="t24 o b">PROBLEME</span>
    </div>
  </div>

  <div class="row t34">WIR SPRECHEN
    <svg width="34" height="34" viewBox="0 0 34 34" aria-hidden="true"><rect x="2" y="2" width="30" height="30" fill="none" stroke="var(--blue)" stroke-width="3"/><path d="M8 17l6 7 13-15" fill="none" stroke="var(--orange)" stroke-width="4"/></svg>
    <span class="o b">KLARTEXT</span></div>

  <div class="split">
    <div class="row" style="gap:10px">
      <span class="icon orange" style="width:50px;height:56px;border-radius:50%" role="img" aria-label="Durchgestrichene Flasche"></span>
      <div class="block">
        <span class="t28 b">UNSERE</span>
        <span class="t28 o b">VORSORGE</span>
        <span class="t14">BRAUCHT KEINEN LIKÖR</span>
      </div>
    </div>
    <div class="divider"></div>
    <div class="row" style="gap:10px">
      <span class="icon" style="width:42px;height:30px" role="img" aria-label="Piktogramm einer rutschenden Figur"></span>
      <div class="block">
        <span class="t28 o b">FEHLER</span>
        <span class="t14">MACHEN IST KEIN</span>
        <span class="t28 o b">FEHLER</span>
      </div>
    </div>
  </div>

  <div class="row t34"><span class="b">DENKVERBOTE</span> SIND <span class="b">TABU</span></div>

  <div class="split">
    <div class="row" style="gap:0">
      <div class="block">
        <span class="big">DENKBAR</span>
        <span class="big o">MACHBAR</span>
      </div>
      <div class="stack-small o"><span>I</span><span>S</span><span>T</span></div>
    </div>
    <div class="divider"></div>
    <div class="block right">
      <span class="t34">VER-</span>
      <span class="t34 b">TRAUEN</span>
      <span class="t14">UM ZU VERTRAUEN</span>
    </div>
  </div>

  <div class="row">
    <span class="icon orange" style="width:46px;height:56px" role="img" aria-label="Piktogramm einer springenden Figur"></span>
    <span class="trau">‘TRAU’ DICH<span class="o">!</span></span>
  </div>

  <div class="split">
    <div class="block">
      <span class="row" style="justify-content:flex-start;gap:10px"><span class="o b" style="font-size:44px">FAIR</span>
        <span class="icon orange" style="width:34px;height:30px" role="img" aria-label="Piktogramm einer Waage"></span></span>
      <span class="t24">ODER GAR NICHT</span>
    </div>
    <div class="divider"></div>
    <div class="row" style="gap:10px">
      <div class="block">
        <span class="t24">WIR GESTALTEN <span class="o b">HEUTE</span></span>
        <span class="t24">UND DENKEN</span>
        <span class="t24">AN <span class="o b spaced">MORGEN</span></span>
      </div>
      <span class="icon orange" style="width:40px;height:44px;border-radius:0 20px 0 20px" role="img" aria-label="Pflanze in Hand"></span>
    </div>
  </div>

  <div class="brand">
    <span class="mark"></span>
    <span class="name">Nordwall</span>
    <span class="sub">Unfall<br>versicherung</span>
  </div>
</main>
</body>
</html>
```